Simple informational site
Target viewers are prime &subcontractors (construction)
• October 15, 2010 7:01 PM reefmortar
Congratulations PlasticBean! Your draft #18 has been finalized as the winner.
• October 15, 2010 7:00 PM reefmortar
Loft42: Thank you for all of your drafts! You really put some thought into the latest ones. We liked your most recent submissions. It was a tough choice. We look forward to seeing more of your work in the future.
• October 15, 2010 6:44 PM Loft42
comments please...............
• October 15, 2010 4:08 PM reefmortar
valdren: Thank you for your drafts. They are being considered.
• October 15, 2010 4:07 PM reefmortar
All
As far as posted times on the draft sites:
1. if TWO times are posted, please label respectively - "Guam" & "Hawaii"
2. if THREE times are posted, please label respectively - "Guam", "Hawaii" and "East Coast"
• October 15, 2010 4:05 PM reefmortar
PlasticBean: we prefer the gray and blue drafts. Also, thank you for including the news feed via RSS.
• October 15, 2010 4:04 PM reefmortar
Loft42: We like the dual-tone shaded site. Thanks.
• October 15, 2010 3:55 PM reefmortar
All - Regarding the "Contact Us" page: we would prefer the page have e-mail capability via a form that has spam prevention capability (e.g. having to enter a random image of letters/numbers).
• October 15, 2010 3:49 PM reefmortar
Loft42: Thank you for your reshaded drafts. We like the dual tone.
• October 15, 2010 3:48 PM reefmortar
All - Thank you for your submissions. Due to the time difference (it is currently 6:45 a.m. where we are located), we were unable to provide immediate feedback. We have approximately 5 hours remaining in our contest. We will begin the draft elimination process shortly; finalization to follow before end of contest.
• October 15, 2010 10:50 AM Loft42
Hi PH, new draft is with light color as per instrcution, waiting for your valuable feedback
Thanks!
• October 15, 2010 9:09 AM PlasticBean
I submitted 2 new drafts with some variation in color, new background and a news section. If they're too dark or if there is anything you don't like let me know. I might work on some different colored versions later on today as well.
• October 15, 2010 6:07 AM reefmortar
PlasticalBean: we find your website the most responsive to our brief and other comments. We would prefer a different background and a bit bolder color scheme. Thank you.
• October 15, 2010 6:05 AM reefmortar
Loft42: Your site is appealing to most members of our team. Some commented that they like the shades of blue background, while others would prefer lighter colors. We feel that the logo looks like it was stuck on the site like a sticker - a bit out of place. Your news feed is very well received.
• October 15, 2010 6:01 AM reefmortar
mulbask: Thank you for your draft. We appreciate the clean design. We have no further comments at this time.
• October 15, 2010 5:57 AM reefmortar
Tenmorvalesh: Your draft sites are clean and simple. We do not have further comments at this time. Thank you.
• October 14, 2010 7:40 AM Loft42
Hi PH, your feedback is welcomed, waiting for your valuable comments if you need any change or variation :)
• October 14, 2010 6:51 AM PlasticBean
I'm glad you like it. Let me know if there's any changes you would like to see.
• October 13, 2010 4:04 PM reefmortar
PlasticBean - we like that your site has a lot of info, but easy to read and navigate. We like that the section headings "grab" our attention well.
• October 13, 2010 4:01 PM reefmortar
Loft42 - thanks for the different versions. We like the details you included: news feed, date and time. The drafts are clean.
• October 13, 2010 2:45 AM reefmortar
reference website in October 11, 2010 4:57 p.m. comment in this discussion string. www.tarnbuildersexample.com
• October 13, 2010 1:46 AM kelodin
Whats the refrence website?
• October 12, 2010 4:19 PM reefmortar
Designers - the Company logo has been finalized. Refer to http://orders.markcraftexample.com/contests/reef-keystone
Regarding questions as to website, we've provided a reference website; the tabs on the referenced site contains almost all that we're looking for.
The site will NOT need links for purchasing.
Home page: should accommodate a brief introduction of the Company and have other pages clearly listed.
Products page: should be able to have products listed. Target customers are prime contractors; technical product data is important. Products include but are not limited to concrete, cement, aggregates, asphalt and tile.
Small business page: should be able to accommodate information as to Company's small business certification which assist federal contractors achieve small business goals
Contact page: should have email inquiry link, Company address and contact numbers
Many prospective contractors do not know much about the island of Guam. We're considering adding a page containing information about Guam.
I hope this helps!
• October 12, 2010 2:17 PM br1ghtsketcher
Hi PH,
Submit will design soon.
Regards
• October 11, 2010 11:50 PM Fl4shPixels
I will submit my design soon.

```html
<!DOCTYPE html>
<html lang="en">
<head>
<meta charset="utf-8">
<title>Reef Keystone</title>
<link href="https://fonts.googleapis.com/css2?family=Oswald:wght@500;600&family=Arimo:wght@400;700&display=swap" rel="stylesheet">
<style>
:root{
  --bg:#3a3b3c;
  --bg-dark:#242526;
  --header:#f1f2f2;
  --ink:#2f3335;
  --nav:#45494c;
  --nav-line:#5c6165;
  --panel-top:#86979f;
  --panel-bot:#4d5b62;
  --side:#aeb9be;
  --side-dark:#7f8d94;
  --white:#ffffff;
  --accent:#f2c400;
  --rss:#f08a1c;
  --text-light:#eef2f3;
  --text-side:#24343c;
}
*{margin:0;padding:0;box-sizing:border-box}
html,body{width:1200px;height:787px;overflow:hidden}
body{background:radial-gradient(ellipse at 50% 40%,#4a4b4c 0%,var(--bg) 45%,var(--bg-dark) 100%);font-family:"Arimo",Arial,sans-serif;position:relative}
.page{position:absolute;left:221px;top:0;width:758px;height:787px}
.site-header{position:absolute;left:0;top:0;width:758px;height:96px;background:linear-gradient(#ffffff,#e3e5e6);}
.brand{position:absolute;left:14px;top:14px;display:flex;align-items:center;gap:10px}
.brand-mark{width:44px;height:44px;background:#5a5f62}
.brand-name{font-family:"Oswald",sans-serif;font-weight:600;font-size:27px;color:#4b5054;letter-spacing:1px;line-height:1}
.brand-tag{position:absolute;left:14px;top:66px;font-size:8px;letter-spacing:1px;color:#5a5f62;text-transform:uppercase;font-weight:700}
.clocks{position:absolute;right:0;top:28px;display:flex}
.clock{width:56px;text-align:center;border-left:1px solid #a9afb2;font-size:12px;color:#4b5054;line-height:20px}
.clock:first-child{border-left:none}
.clock .time{color:#2d6d9a}
.main-nav{position:absolute;left:0;top:96px;width:211px;height:173px;background:var(--nav)}
.main-nav a{display:block;height:34.6px;line-height:34px;padding-left:14px;border-bottom:1px solid var(--nav-line);color:var(--white);font-weight:700;font-size:13px;text-decoration:none}
.hero{position:absolute;left:211px;top:96px;width:547px;height:173px;background:linear-gradient(100deg,#7b8a91 0%,#c9cfd1 35%,#e8e3d6 55%,#9aa5a8 80%,#6f7c82 100%)}
.content{position:absolute;left:0;top:269px;width:554px;height:494px;background:linear-gradient(var(--panel-top),var(--panel-bot) 50%,var(--panel-top) 50%,var(--panel-bot))}
.feature{position:absolute;left:0;width:554px}
.feature-head{position:relative;height:80px;background:linear-gradient(90deg,#3c474d,#57656c 60%,#8797a0);border-bottom:2px solid #2c3438}
.feature-head h2{position:absolute;left:14px;top:20px;font-family:"Oswald",sans-serif;font-weight:600;font-size:29px;color:var(--white);text-shadow:1px 1px 2px #1c2226}
.feature-img{position:absolute;right:0;top:0;width:220px;height:80px}
.feature p{color:var(--text-light);font-size:13.2px;line-height:15px;margin:10px 14px 0;width:470px}
.feature p.small{font-size:9px;line-height:11px;width:520px;color:#dfe5e8}
.feature strong{color:var(--white)}
.more{color:var(--accent);font-size:8.5px}
.sidebar{position:absolute;left:554px;top:269px;width:204px;height:494px;background:linear-gradient(var(--side),#c9d1d4 40%,var(--side) 100%);border-left:2px solid #3c474d}
.side-head{font-family:"Oswald",sans-serif;font-weight:600;color:var(--white);font-size:25px;text-shadow:1px 1px 2px #4d5b62;padding-left:10px}
.side-text{font-size:9px;line-height:11px;color:var(--text-side);padding:0 10px}
.who{position:absolute;top:10px;left:0;width:204px}
.news{position:absolute;top:140px;left:0;width:204px;padding:0 10px}
.news h3{font-size:14px;color:var(--white);font-weight:700;display:flex;align-items:center;gap:6px;margin-bottom:8px}
.rss{width:13px;height:13px;background:var(--rss);border-radius:2px}
.news-item{margin-bottom:12px}
.news-item .title{color:#2d6d9a;font-size:8.5px;font-weight:700}
.news-item p{font-size:8px;line-height:10px;color:var(--text-side)}
.contact{position:absolute;top:320px;left:0;width:204px}
.contact .side-head{display:flex;align-items:center;gap:8px;font-size:27px}
.contact dl{padding:8px 14px 0}
.contact dt{font-size:10px;color:#2d5c74}
.contact dd{font-family:"Oswald",sans-serif;font-weight:500;font-size:20px;color:var(--white);margin-bottom:6px;letter-spacing:.5px}
.social{display:flex;gap:4px;padding-left:95px;margin-top:-2px}
.social span{width:14px;height:14px;background:#3f6f97;border-radius:2px}
.site-footer{position:absolute;left:0;top:763px;width:758px;height:24px;background:#d9dddf;font-size:8px;color:#4b5054;line-height:24px;padding-left:10px}
</style>
</head>
<body>
<div class="page">
  <header class="site-header">
    <div class="brand"><div class="brand-mark"></div><div class="brand-name">REEF KEYSTONE</div></div>
    <div class="brand-tag">Premier wholesaler of construction materials</div>
    <div class="clocks">
      <div class="clock"><div>GMT +10</div><div class="time">8:32 PM</div></div>
      <div class="clock"><div>GMT -8</div><div class="time">11:32 AM</div></div>
      <div class="clock"><div>GMT +8</div><div class="time">8:32 PM</div></div>
    </div>
  </header>

  <nav class="main-nav">
    <a href="#">Home</a><a href="#">Products</a><a href="#">About Us</a><a href="#">About Guam</a><a href="#">Contact Us</a>
  </nav>
  <div class="hero" role="img" aria-label="Photo of a smiling construction worker in a yellow hard hat beside rail tracks"></div>

  <main class="content">
    <section class="feature" style="top:0">
      <div class="feature-head">
        <div class="feature-img" role="img" aria-label="Photo of fresh concrete and gravel" style="background:linear-gradient(90deg,rgba(87,101,108,0),#9aa3a6 40%,#c3c6c4 70%,#8c9396)"></div>
        <h2>Only The Finest Products</h2>
      </div>
      <p>We don't mess around when it comes to our products.<br><strong>We take pride in what we produce</strong> and carry only the top products for a result that will last a lifetime.</p>
      <p class="small">Lorem ipsum dolor sit amet, consectetur adipiscing elit. Quisque volutpat sapien a tellus blandit id commodo lorem commodo. Proin a eros libero, nec adipiscing tellus. Integer ultricies, arcu quis tempus aliquet, lacus nibh placerat eros, ut varius orci ligula vel est. Maecenas leo dolor, porttitor vel facilisis feugiat, semper eget nunc. <span class="more">Read More</span></p>
    </section>
    <section class="feature" style="top:240px">
      <div class="feature-head">
        <div class="feature-img" role="img" aria-label="Photo of an open road through green fields" style="background:linear-gradient(90deg,rgba(87,101,108,0),#a7b3b8 40%,#d9dfe1 70%,#7f9a6a)"></div>
        <h2>Get Your Job Moving With Us</h2>
      </div>
      <p>Tired of waiting around for the necessary materials you need to get the job done? <strong>Well don't wait any longer.</strong> We get our products out faster than our competition, guaranteed.</p>
      <p class="small">Lorem ipsum dolor sit amet, consectetur adipiscing elit. Quisque volutpat sapien a tellus blandit id commodo lorem commodo. Proin a eros libero, nec adipiscing tellus. Integer ultricies, arcu quis tempus aliquet, lacus nibh placerat eros, ut varius orci ligula vel est. Maecenas leo dolor, porttitor vel facilisis feugiat, semper eget nunc. <span class="more">Read More</span></p>
    </section>
  </main>

  <aside class="sidebar">
    <div class="who">
      <h2 class="side-head">Who We Are</h2>
      <p class="side-text">We are a woman owned business that's small enough to care and large enough to be efficient. <span class="more">Read More</span></p>
    </div>
    <div class="news">
      <h3>Local News <span class="rss"></span></h3>
      <div class="news-item"><div class="title">Local News Title Goes Here</div><p>Lorem ipsum dolor sit amet, consectetur adipiscing elit.</p></div>
      <div class="news-item"><div class="title">Local News Title Goes Here</div><p>Lorem ipsum dolor sit amet, consectetur adipiscing elit.</p></div>
      <div class="news-item"><div class="title">Local News Title Goes Here</div><p>Lorem ipsum dolor sit amet, consectetur adipiscing elit.</p></div>
    </div>
    <div class="contact">
      <h2 class="side-head">Contact Us
        <svg width="34" height="24" viewBox="0 0 34 24" aria-hidden="true"><path d="M4 20 Q4 4 17 4 Q30 4 30 20 Z" fill="#f2c400"/><rect x="1" y="19" width="32" height="4" rx="2" fill="#d9a800"/></svg>
      </h2>
      <dl>
        <dt>Tel:</dt><dd>800-123-1234</dd>
        <dt>Toll Free:</dt><dd>800-123-1234</dd>
      </dl>
      <div class="social"><span></span><span></span><span></span></div>
    </div>
  </aside>

  <footer class="site-footer">©2010 Reef Keystone, Inc. | Privacy Policy</footer>
</div>
</body>
</html>
```